HVAC company business card design

We need a business card design for a HVAC company. The design must look professional. Both sides will be used. The total data to be on the business card is
Name
Position
Email
Direct Phone/Moile Phone
Company Contacts /Address, Phone, Fax, web)
All data will be submit once the design is confirmed. For generic purposes use;
Emre Toksoy
Managing Director
+902324815263 (Mobile)
4712 Sokak No: 9 KBSE Yenikent IZMIR TURKEY
Tel: +902324815263 Fax : +902324815269
www.luvon.com.tr

Target Market(s)

HVAC

Industry/Entity Type

Business

Contact Information for Business Card

The total data to be on the business card is
Name
Position
Email
Direct Phone/Moile Phone
Emre Toksoy
Managing Director
+902324815263 (Mobile)
www.luvon.com.tr
The BC will use both sides of the card. The front will include the full logo and the details for the business card holder. The business card can be divided into vertical/horizontal or to a special shape. The common data like the company address/phone/fax should be indicated elsewehere. The back can contain some part or the whole logo and must contain the web address.

Font styles to use
Serif
Sans Serif

Colors
0355a3
cfdfed

Requirements
Should not have
• Please be careful with the fonts, it shouldnt be too small or too big and must not interfere with the logo fonts. If you need to use a curvy shape please do not use as the logo is already curvy or use the curves from the logo (if it looks good, otherwise forget it)
• We are not in favor of pictograms, only if they are perfect use them.

```html
<!DOCTYPE html>
<html lang="en">
<head>
<meta charset="utf-8">
<title>LUVON Business Card</title>
<link rel="stylesheet" href="https://fonts.googleapis.com/css2?family=Exo+2:wght@400;500;600;700&display=swap">
<style>
  :root {
    --page: #d9d9db;
    --card-front: #ececee;
    --navy: #373d57;
    --blue: #2c5fbf;
    --ink: #3b3b40;
    --rule: #a9aab0;
    --white: #ffffff;
  }
  * { margin: 0; padding: 0; box-sizing: border-box; }
  html, body {
    width: 1105px; height: 1200px; overflow: hidden;
    background: var(--page);
    font-family: "Exo 2", Arial, sans-serif;
  }
  .card {
    position: absolute; left: 182px; width: 746px; height: 426px;
  }
  .card--front { top: 120px; background: var(--card-front); }
  .card--back { top: 637px; background: var(--navy); }

  .brand-tab {
    position: absolute; left: 0; top: 59px; width: 25px; height: 97px;
    background: var(--navy);
  }
  .brand-dot {
    position: absolute; left: 36px; top: 62px; width: 90px; height: 90px;
    border-radius: 50%; background: var(--blue);
  }
  .brand-name {
    position: absolute; left: 142px; top: 60px;
    font-size: 66px; font-weight: 600; letter-spacing: 2px; line-height: 1;
    color: var(--navy);
  }

  .holder { position: absolute; left: 142px; top: 212px; }
  .holder-name { font-size: 26px; font-weight: 600; color: var(--blue); line-height: 1.2; }
  .holder-role { font-size: 19px; color: var(--ink); line-height: 1.4; }

  .contact-list {
    position: absolute; left: 142px; top: 298px; list-style: none;
    font-size: 21px; color: var(--ink); letter-spacing: 1px;
  }
  .contact-list li { display: flex; align-items: center; height: 28.5px; }
  .contact-list svg { width: 18px; height: 18px; margin-right: 15px; fill: var(--blue); }

  .divider {
    position: absolute; left: 388px; top: 294px; width: 1px; height: 100px;
    background: var(--rule);
  }
  .office {
    position: absolute; left: 411px; top: 298px;
    font-size: 20px; color: var(--ink); font-style: normal; letter-spacing: 0.5px;
  }
  .office span { display: block; height: 28.5px; line-height: 28.5px; }
  .office .web { color: var(--blue); letter-spacing: 2px; }

  .back-name {
    position: absolute; left: 0; right: 0; top: 168px; text-align: center;
    font-size: 72px; font-weight: 600; letter-spacing: 3px; line-height: 1;
    color: var(--white);
  }
  .back-web {
    position: absolute; left: 0; right: 0; top: 346px; text-align: center;
    font-size: 19px; letter-spacing: 6px; color: var(--white);
  }
</style>
</head>
<body>
  <section class="card card--front">
    <div class="brand-tab"></div>
    <div class="brand-dot"></div>
    <div class="brand-name">LUVON</div>

    <div class="holder">
      <div class="holder-name">Emre Toksoy</div>
      <div class="holder-role">Managing Director</div>
    </div>

    <ul class="contact-list">
      <li>
        <svg viewBox="0 0 24 24" aria-hidden="true"><path d="M6.6 10.8a15.1 15.1 0 0 0 6.6 6.6l2.2-2.2a1 1 0 0 1 1-.25 11.4 11.4 0 0 0 3.6.57 1 1 0 0 1 1 1V20a1 1 0 0 1-1 1A17 17 0 0 1 3 4a1 1 0 0 1 1-1h3.5a1 1 0 0 1 1 1c0 1.25.2 2.45.57 3.57a1 1 0 0 1-.25 1z"/></svg>
        +902324815263
      </li>
      <li>
        <svg viewBox="0 0 24 24" aria-hidden="true"><path d="M7 1h10a2 2 0 0 1 2 2v18a2 2 0 0 1-2 2H7a2 2 0 0 1-2-2V3a2 2 0 0 1 2-2zm0 3v14h10V4zm5 15.5a1 1 0 1 0 0 2 1 1 0 0 0 0-2z"/></svg>
        +902324815263
      </li>
      <li>
        <svg viewBox="0 0 24 24" aria-hidden="true"><path d="M6 2h9l3 3v4H6zM3 10h18a1 1 0 0 1 1 1v7h-3v-3H5v3H2v-7a1 1 0 0 1 1-1zm4 7h10v5H7z"/></svg>
        +902324815269
      </li>
    </ul>

    <div class="divider"></div>

    <address class="office">
      <span>4712 Sokak No: 9 KBSE</span>
      <span>Yenikent IZMIR TURKEY</span>
      <span class="web">www.luvon.com.tr</span>
    </address>
  </section>

  <section class="card card--back">
    <div class="back-name">LUVON</div>
    <div class="back-web">www.luvon.com.tr</div>
  </section>
</body>
</html>
```